Progressive/contemporary business card design for successful Startups as a Service Company

New logo launched in 2020. New website launched in 2021. Now that COVID is (mostly) behind us, I'm networking with more people and need a business card that matches the company/logo design aesthetic.

```html
<!DOCTYPE html>
<html lang="en">
<head>
<meta charset="utf-8">
<title>BuildNext business card</title>
<link rel="stylesheet" href="https://fonts.googleapis.com/css2?family=Montserrat:wght@400;500;700&family=Arimo:wght@400;700&display=swap">
<style>
  :root {
    --stage: #141414;
    --card: #1e1e1e;
    --card-edge: #262626;
    --pattern-a: #2a2a2a;
    --pattern-b: #161616;
    --ink: #ffffff;
    --ink-soft: #cfcfcf;
    --accent: #f5c21b;
    --rule: #8a8a8a;
  }
  * { box-sizing: border-box; margin: 0; padding: 0; }
  html, body { width: 1200px; height: 963px; overflow: hidden; }
  body {
    background: var(--stage);
    display: flex;
    flex-direction: column;
    align-items: center;
    justify-content: center;
    gap: 60px;
    font-family: "Arimo", Arial, sans-serif;
    color: var(--ink);
  }
  .card {
    position: relative;
    width: 560px;
    height: 320px;
    background: var(--card);
    border: 1px solid var(--card-edge);
    box-shadow: 0 18px 40px rgba(0,0,0,.6);
    overflow: hidden;
  }
  .wordmark {
    display: flex;
    align-items: center;
    gap: 14px;
    font-family: "Montserrat", Arial, sans-serif;
    font-weight: 500;
    color: var(--ink);
    letter-spacing: 0.22em;
    font-size: 34px;
  }
  .wordmark .mark {
    width: 26px;
    height: 26px;
    background: var(--accent);
  }
  .card--front .wordmark {
    position: absolute;
    top: 58px;
    left: 50%;
    transform: translateX(-50%);
    white-space: nowrap;
  }
  .contact-block {
    position: absolute;
    top: 168px;
    left: 0;
    right: 0;
    display: flex;
    justify-content: center;
    align-items: center;
    gap: 22px;
  }
  .person { text-align: right; }
  .person-name {
    font-weight: 700;
    color: var(--accent);
    text-transform: uppercase;
    font-size: 15px;
    letter-spacing: 0.02em;
  }
  .person-role {
    font-size: 14px;
    color: var(--ink);
    margin-top: 3px;
  }
  .divider {
    width: 1px;
    height: 62px;
    background: var(--rule);
  }
  .details { list-style: none; font-size: 13.5px; }
  .details li {
    display: flex;
    align-items: center;
    gap: 8px;
    line-height: 20px;
  }
  .details svg { width: 13px; height: 13px; fill: var(--accent); flex: none; }
  .address {
    position: absolute;
    bottom: 44px;
    left: 0;
    right: 0;
    text-align: center;
    font-size: 13.5px;
    color: var(--ink);
  }
  .card--back .pattern {
    position: absolute;
    inset: 0;
    background: linear-gradient(135deg, var(--pattern-a), var(--pattern-b) 55%, var(--pattern-a));
  }
  .card--back .wordmark {
    position: absolute;
    top: 50%;
    left: 50%;
    transform: translate(-50%, -50%);
    white-space: nowrap;
    font-size: 30px;
  }
</style>
</head>
<body>

  <section class="card card--front" aria-label="Card front">
    <div class="wordmark"><span>BUILDNEXT</span><span class="mark"></span></div>

    <div class="contact-block">
      <div class="person">
        <div class="person-name">Dana Whitfield</div>
        <div class="person-role">Manager</div>
      </div>
      <div class="divider"></div>
      <ul class="details">
        <li>
          <svg viewBox="0 0 16 16" aria-hidden="true"><path d="M3.6 1.2l2.4 2.6-1.4 1.8c.9 2 2.4 3.6 4.6 4.7l1.8-1.4 2.6 2.4-1.6 2.4C6.8 13.5 2.5 9.2 1.3 2.8z"/></svg>
          555-018-2100
        </li>
        <li>
          <svg viewBox="0 0 16 16" aria-hidden="true"><path d="M1 3h14v10H1zM2 4.2v.4l6 4.4 6-4.4v-.4z"/></svg>
          hello@buildnext.co
        </li>
        <li>
          <svg viewBox="0 0 16 16" aria-hidden="true"><path d="M8 1a7 7 0 1 0 0 14A7 7 0 0 0 8 1zm0 1.6c.8.9 1.4 2.3 1.6 4H6.4c.2-1.7.8-3.1 1.6-4zM6.4 8.4h3.2c-.2 1.7-.8 3.1-1.6 4-.8-.9-1.4-2.3-1.6-4zM2.7 7.6c.2-1.8 1.4-3.4 3-4.2-.5 1.1-.9 2.6-1 4.2zm0 .8h2c.1 1.6.5 3.1 1 4.2-1.6-.8-2.8-2.4-3-4.2zm10.6 0c-.2 1.8-1.4 3.4-3 4.2.5-1.1.9-2.6 1-4.2zm0-.8h-2c-.1-1.6-.5-3.1-1-4.2 1.6.8 2.8 2.4 3 4.2z"/></svg>
          www.buildnext.co
        </li>
      </ul>
    </div>

    <div class="address">Your address, city, state, ZIP 0000</div>
  </section>

  <section class="card card--back" aria-label="Card back">
    <div class="pattern" role="img" aria-label="Embossed dark geometric triangle pattern"></div>
    <div class="wordmark"><span>BUILDNEXT</span><span class="mark"></span></div>
  </section>

</body>
</html>
```